Copper Kite Pastimes- Retailer

Need to describe what Copper Kite Pastimes is, what products we carry with photos and descriptions, as well as pricing for each. shopping cart, purchase items by way of Zellpay and CoinDrift

Industry/Entity Type

Hobby / Entertainment

Coding

Coded - Design and coding required

Number of Pages Required

5+ page

Font styles to use
Sans Serif

Colors
0054AA
0677BA
7BADD7
CADEEF
E8F1F8
F0912C
F2A743
F7CA91
FBE8D2
FDF5EE
EE7325
F08F49
F5BC92
FAE3D3
FDF4ED

Requirements
Must have
• Product pages, shopping cart, checkout
Nice to have
• Video/gif, of working train or slot car tracks
Should not have
• Cartoon characters or images

```html
<!DOCTYPE html>
<html lang="en">
<head>
<meta charset="utf-8">
<title>Copper Kite Pastimes</title>
<link href="https://fonts.googleapis.com/css2?family=Plus+Jakarta+Sans:wght@400;500;600;700;800&display=swap" rel="stylesheet">
<style>
:root{
  --navy:#1e2430;
  --blue-deep:#0054aa;
  --blue:#0677ba;
  --blue-soft:#7badd7;
  --blue-pale:#e8f1f8;
  --orange:#f0912c;
  --orange-light:#f2a743;
  --orange-deep:#ee7325;
  --peach:#fbe8d2;
  --cream:#fdf5ee;
  --ink:#1e2430;
  --muted:#5b6170;
  --white:#ffffff;
}
*{box-sizing:border-box;margin:0;padding:0}
html,body{width:1200px;height:5204px;overflow:hidden}
body{font-family:"Plus Jakarta Sans",Arial,sans-serif;color:var(--ink);background:#fff;font-size:14px}
.wrap{width:1080px;margin:0 auto;position:relative}
.soft{-webkit-mask-image:radial-gradient(ellipse at center,#000 50%,transparent 74%);mask-image:radial-gradient(ellipse at center,#000 50%,transparent 74%)}

/* header */
.topbar{height:97px;background:var(--navy);display:flex;align-items:center;padding:0 60px;gap:130px}
.brand{display:flex;align-items:center;gap:8px;color:var(--white);font-weight:700;font-size:13px;line-height:1.1;width:140px}
.brand-mark{width:14px;height:14px;border-radius:50%;background:var(--orange);flex:none}
.search{display:flex;width:540px;height:44px;border-radius:8px;overflow:hidden;background:#fff}
.search-field{flex:1;display:flex;align-items:center;gap:10px;padding:0 16px;color:#555;font-size:13px}
.search-btn{width:122px;background:var(--orange);color:#fff;font-weight:700;font-size:13px;display:flex;align-items:center;justify-content:center}
.top-icons{margin-left:auto;display:flex;gap:22px}
.navbar{height:48px;background:var(--blue-deep);display:flex;justify-content:center;align-items:center;gap:34px;color:#fff;font-size:13px;font-weight:500}
.navbar .caret::after{content:"";display:inline-block;margin-left:6px;border:4px solid transparent;border-top-color:#fff;transform:translateY(2px)}

.categories{height:152px;display:flex;justify-content:space-between;padding:18px 64px 0}
.cat{width:90px;text-align:center;font-size:11px;font-weight:600}
.cat-img{width:86px;height:86px;border-radius:50%;margin:0 auto 14px;background:var(--blue-pale);position:relative;overflow:hidden}
.cat-img::after{content:"";position:absolute;left:14px;right:14px;top:26px;bottom:26px;border-radius:10px;background:var(--tone);-webkit-mask-image:radial-gradient(ellipse,#000 45%,transparent 72%);mask-image:radial-gradient(ellipse,#000 45%,transparent 72%)}

/* hero */
.hero{height:623px;background:radial-gradient(circle at 50% 55%,#fbe39a 0%,#f7cf55 45%,#f2b93c 100%);position:relative;text-align:center;padding-top:70px}
.hero h1{font-size:56px;font-weight:800;line-height:1.18;letter-spacing:-1px}
.hero h1 .o{color:var(--orange)}
.hero h1 .b{color:var(--blue-deep)}
.btn-solid{display:inline-block;background:var(--orange);color:#fff;font-size:11px;font-weight:600;padding:13px 38px;border-radius:3px}
.hero .btn-solid{margin-top:20px}
.hero-art{position:absolute;left:60px;right:60px;bottom:40px;height:310px;background:linear-gradient(90deg,#f3b51e 0%,#e9a514 14%,#c8232b 26%,#b01e24 36%,#b9bdc6 48%,#8a8f99 56%,#1d55b0 68%,#16408a 76%,#2a2b30 88%,#3a2d22 100%);-webkit-mask-image:radial-gradient(ellipse 52% 60% at 50% 58%,#000 55%,transparent 100%);mask-image:radial-gradient(ellipse 52% 60% at 50% 58%,#000 55%,transparent 100%)}

/* about */
.about{height:494px;padding-top:78px}
.about .wrap{display:flex;justify-content:space-between}
.about-text{width:540px}
.h-sec{font-size:38px;font-weight:800;line-height:1.2;letter-spacing:-.5px}
.h-sec .o{color:var(--orange-deep)}
.about-text p{color:var(--muted);font-size:13px;line-height:1.6;margin-top:22px;width:530px}
.ticks{list-style:none;margin-top:20px}
.ticks li{display:flex;align-items:center;gap:10px;font-size:12px;font-weight:600;margin-bottom:14px}
.ticks .dot{width:16px;height:16px;border-radius:50%;background:var(--orange);display:flex;align-items:center;justify-content:center}
.about .btn-solid{margin-top:10px;padding:14px 52px}
.about-art{position:relative;width:440px;height:390px;margin-top:-6px}
.about-frame{position:absolute;right:0;top:0;width:210px;height:330px;background:var(--orange)}
.about-photo{position:absolute;left:8px;top:30px;width:420px;height:300px;background:linear-gradient(120deg,#cadeef 0%,#e8c3a6 30%,#f0d6c2 45%,#5b8fc4 62%,#0677ba 80%,#7badd7 100%);border:6px solid var(--orange)}
.wheel{position:absolute;bottom:0;width:120px;height:120px;border-radius:50%;background:var(--orange)}

/* section heads */
.sec-head{text-align:center}
.sec-head p{color:var(--muted);font-size:13px;line-height:1.5;margin:8px auto 0;width:460px}

/* products */
.favorites{height:1125px;padding-top:86px}
.prod-grid{display:grid;grid-template-columns:repeat(3,332px);gap:61px 42px;margin-top:62px}
.prod{height:316px;border-radius:6px;color:#fff;text-align:center;padding:22px 24px}
.prod.blue{background:var(--blue)}
.prod.orange{background:var(--orange)}
.prod.deep{background:var(--orange-deep)}
.prod.dark{background:var(--navy)}
.prod-img{height:110px;margin:0 10px 26px}
.prod .scale{font-size:12px;font-weight:600}
.prod h3{font-size:13px;font-weight:700;line-height:1.3;margin-top:12px}
.prod .price{font-size:21px;font-weight:700;margin-top:12px}
.btn-outline{display:inline-block;border:1.5px solid #fff;border-radius:4px;padding:8px 22px;font-size:11px;font-weight:600;margin-top:18px}
.center{text-align:center}
.favorites .btn-solid{margin-top:60px;padding:12px 28px}

/* confidence */
.confidence{height:400px}
.conf-grid{display:grid;grid-template-columns:repeat(4,262px);gap:12px;margin-top:62px;margin-left:-2px}
.conf{height:172px;color:#fff;text-align:center;padding-top:36px}
.conf.blue{background:var(--blue)}
.conf.orange{background:var(--orange)}
.conf.dark{background:var(--navy)}
.conf.deep{background:var(--orange-deep)}
.conf h4{font-size:15px;font-weight:700;margin-top:12px}
.conf p{font-size:11px;line-height:1.35;margin-top:4px;opacity:.9}

/* brands */
.brands{height:333px}
.brand-row{display:flex;justify-content:space-between;align-items:center;margin-top:56px;height:110px}
.brand-name{font-size:20px;font-weight:700;color:var(--navy);display:flex;align-items:center;gap:10px}
.brand-name .sq{width:20px;height:20px;border-radius:50%;background:var(--blue-deep)}

/* reviews */
.reviews{height:374px;position:relative}
.rev-grid{display:grid;grid-template-columns:repeat(3,312px);gap:48px;margin:68px auto 0;width:1032px}
.rev{height:172px;border-radius:4px;color:#fff;padding:18px 20px}
.rev.dark{background:var(--navy)}
.rev.orange{background:var(--orange)}
.rev.blue{background:var(--blue)}
.stars{color:var(--orange-light);font-size:15px;letter-spacing:3px}
.rev.orange .stars{color:#fde68a}
.rev p{font-size:11px;line-height:1.4;margin-top:6px}
.reviewer{display:flex;align-items:center;gap:10px;margin-top:12px;font-size:11px}
.avatar{width:32px;height:32px;border-radius:50%;background:var(--peach);flex:none}
.reviewer small{display:block;font-size:10px;opacity:.85}
.arrow{position:absolute;top:230px;font-size:22px;color:#333}

/* faq */
.faq{height:642px;background:var(--navy);padding-top:62px;color:#fff}
.faq .h-sec .o{color:var(--orange)}
.faq .sec-head p{color:#c9cdd6}
.faq-list{width:590px;margin:48px auto 0}
.faq-item{background:#fff;color:var(--ink);border-radius:4px;height:50px;display:flex;justify-content:space-between;align-items:stretch;margin-bottom:22px;font-size:12px;font-weight:500}
.faq-item span{padding-left:18px;align-self:center}
.faq-plus{width:52px;display:flex;align-items:center;justify-content:center;color:#fff;font-size:20px;border-radius:0 4px 4px 0}
.faq-plus.blue{background:var(--blue)}
.faq-plus.orange{background:var(--orange)}
.faq-open{background:#fff;color:var(--ink);border-radius:4px;height:180px;padding:18px;font-size:12px;font-weight:500}
.faq-open p{color:#6b7180;font-size:11px;line-height:1.7;margin-top:22px;font-weight:400}

/* cta */
.cta{height:535px;background:linear-gradient(180deg,#fdf5ee,#f7f3ee);position:relative}
.cta-card{position:absolute;left:60px;top:115px;width:1080px;height:346px;background:radial-gradient(circle at 75% 50%,#f5bc92,#f2a743 45%,#ee7325);color:#fff;padding:74px 42px;box-shadow:0 8px 20px rgba(0,0,0,.12)}
.cta-card h2{font-size:38px;font-weight:800;line-height:1.28;text-transform:uppercase}
.cta-card p{font-size:13px;line-height:1.6;margin-top:20px;width:480px}
.cta-card .btn-outline{margin-top:18px;padding:12px 52px;border-radius:2px}
.cta-art{position:absolute;left:720px;top:35px;width:440px;height:390px}
.cta-frame{position:absolute;right:0;top:0;width:220px;height:360px;background:var(--navy)}
.cta-photo{position:absolute;left:0;top:40px;width:430px;height:330px;background:linear-gradient(135deg,#3a4a5a 0%,#7badd7 25%,#1aa0d8 50%,#0677ba 70%,#e0b08a 100%);border:6px solid var(--navy)}

/* footer */
.footer{height:407px;background:var(--navy);color:#fff;padding:48px 60px 0;position:relative}
.foot-grid{display:flex}
.foot-brand{width:328px;padding-top:10px}
.foot-logo{display:flex;align-items:center;gap:10px;font-size:20px;font-weight:700;margin-left:70px}
.foot-brand p{font-size:11px;line-height:1.4;text-align:center;width:240px;margin-top:80px}
.foot-col{width:160px}
.foot-col h5{font-size:15px;font-weight:700;margin-bottom:10px}
.foot-col a{display:flex;align-items:center;gap:7px;color:#fff;text-decoration:none;font-size:12px;line-height:1.95}
.foot-col .ic{width:11px;height:11px;border:1.5px solid #fff;border-radius:3px}
.foot-join{width:280px}
.foot-join h5{font-size:15px;font-weight:700}
.foot-join p{font-size:11px;line-height:1.4;margin-top:8px}
.news{display:flex;gap:10px;margin-top:24px}
.news-input{width:222px;height:42px;background:#fff;border-radius:2px;color:#888;font-size:9px;display:flex;align-items:center;padding-left:14px}
.news-btn{width:42px;height:42px;background:var(--orange);border-radius:2px;display:flex;align-items:center;justify-content:center}
.pay h5{margin-top:22px;font-size:15px}
.pay-badges{display:flex;gap:12px;margin-top:10px}
.pay-badge{width:54px;height:38px;background:#fff;border-radius:4px;color:var(--blue-deep);font-size:10px;font-weight:700;display:flex;align-items:center;justify-content:center}
.foot-bottom{position:absolute;left:60px;right:60px;bottom:76px;display:flex;font-size:10px}
.foot-bottom .links{margin-left:auto;display:flex;gap:20px}
</style>
</head>
<body>

<header class="topbar">
  <div class="brand"><span class="brand-mark"></span><span>Copper Kite<br>Pastimes</span></div>
  <div class="search">
    <div class="search-field">
      <svg width="14" height="14" viewBox="0 0 24 24" fill="none" stroke="#555" stroke-width="2.5"><circle cx="10" cy="10" r="7"/><path d="M15 15l6 6"/></svg>
      Search Products
    </div>
    <div class="search-btn">Search</div>
  </div>
  <div class="top-icons">
    <svg width="16" height="16" viewBox="0 0 24 24" fill="none" stroke="#fff" stroke-width="2"><path d="M12 20s-8-5-8-11a4 4 0 0 1 8-1 4 4 0 0 1 8 1c0 6-8 11-8 11z"/></svg>
    <svg width="16" height="16" viewBox="0 0 24 24" fill="none" stroke="#fff" stroke-width="2"><path d="M3 4h3l2 11h11l2-8H7"/><circle cx="9" cy="20" r="1.5"/><circle cx="18" cy="20" r="1.5"/></svg>
    <svg width="16" height="16" viewBox="0 0 24 24" fill="none" stroke="#fff" stroke-width="2"><circle cx="12" cy="8" r="4"/><path d="M4 21c1-5 15-5 16 0"/></svg>
  </div>
</header>

<nav class="navbar">
  <span>Home</span><span>All Products</span><span class="caret">Car Models</span><span class="caret">Shop By Scale</span><span>Track Order</span><span>About</span>
</nav>

<section class="categories">
  <div class="cat"><div class="cat-img" style="--tone:linear-gradient(90deg,#9aa0aa,#d7dbe0)" role="img" aria-label="Die-cast truck model"></div>Die-Cast Trucks</div>
  <div class="cat"><div class="cat-img" style="--tone:linear-gradient(90deg,#2a2a2e,#b0232a)" role="img" aria-label="Model train locomotive"></div>Trains</div>
  <div class="cat"><div class="cat-img" style="--tone:linear-gradient(90deg,#e9c31c,#3a3a3a)" role="img" aria-label="Model motorbike"></div>Bikes</div>
  <div class="cat"><div class="cat-img" style="--tone:linear-gradient(90deg,#c8232b,#e9ecef)" role="img" aria-label="Model trailer truck"></div>Trailers</div>
  <div class="cat"><div class="cat-img" style="--tone:linear-gradient(90deg,#ee7325,#f2a743)" role="img" aria-label="Orange slot car"></div>Slot Cars</div>
  <div class="cat"><div class="cat-img" style="--tone:linear-gradient(90deg,#3a3f47,#7a808a)" role="img" aria-label="Model off-road jeep"></div>Jeeps</div>
  <div class="cat"><div class="cat-img" style="--tone:linear-gradient(90deg,#2f5a2a,#222)" role="img" aria-label="Model monster truck"></div>Monster Trucks</div>
</section>

<section class="hero">
  <h1><span class="o">Build Your Dream</span> <span class="b">Garage</span><br><span class="b">New Arrivals Just Landed.</span></h1>
  <span class="btn-solid">EXPLORE MORE</span>
  <div class="hero-art" role="img" aria-label="Lineup of model vehicles: school bus, big rig trucks, muscle car and steam locomotive"></div>
</section>

<section class="about">
  <div class="wrap">
    <div class="about-text">
      <h2 class="h-sec"><span class="o">WHAT IS</span> COPPER KITE<br>PASTIMES?</h2>
      <p>in a world dominated by screens, copper kite pastimes exists to bring back hands-on entertainment, collecting, building, and imagination.</p>
      <p style="margin-top:18px">we help hobbyists, collectors, parents, and enthusiasts discover products that inspire creativity and create lasting memories.</p>
      <ul class="ticks">
        <li><span class="dot"><svg width="9" height="9" viewBox="0 0 10 10"><path d="M2 5l2 2 4-4" stroke="#fff" stroke-width="1.8" fill="none"/></svg></span>COD Delivery</li>
        <li><span class="dot"><svg width="9" height="9" viewBox="0 0 10 10"><path d="M2 5l2 2 4-4" stroke="#fff" stroke-width="1.8" fill="none"/></svg></span>100% Authentic</li>
        <li><span class="dot"><svg width="9" height="9" viewBox="0 0 10 10"><path d="M2 5l2 2 4-4" stroke="#fff" stroke-width="1.8" fill="none"/></svg></span>Fast &amp; Reliable Shipping</li>
      </ul>
      <span class="btn-solid">LEARN MORE</span>
    </div>
    <div class="about-art">
      <div class="about-frame"></div>
      <div class="about-photo" role="img" aria-label="Parent and child playing with a blue model car"></div>
      <div class="wheel" style="left:60px"></div>
      <div class="wheel" style="left:275px"></div>
    </div>
  </div>
</section>

<section class="favorites">
  <div class="wrap">
    <div class="sec-head">
      <h2 class="h-sec"><span class="o">COLLECTOR</span> FAVORITES</h2>
      <p>The models collectors can't stop talking about. bring back hands-on entertainment, collecting, building, and imagination.</p>
    </div>
    <div class="prod-grid">
      <div class="prod blue"><div class="prod-img soft" style="background:linear-gradient(180deg,#f5c21b 0%,#f2b312 60%,#2a2a2e 100%)" role="img" aria-label="Yellow school bus model"></div><div class="scale">1/64 Scale</div><h3>School Bus KT Bus Internal<br>Combustion (ICE) School Bus</h3><div class="price">$545.99</div><span class="btn-outline">Add to cart</span></div>
      <div class="prod orange"><div class="prod-img soft" style="background:linear-gradient(90deg,#f4f6f8 0%,#c9ced6 40%,#e3e6ea 70%,#9aa0aa 100%)" role="img" aria-label="Silver tanker truck model"></div><div class="scale">1/64 Scale</div><h3>School Bus KT Bus Internal<br>Combustion (ICE) School Bus</h3><div class="price">$545.99</div><span class="btn-outline">Add to cart</span></div>
      <div class="prod dark"><div class="prod-img soft" style="background:linear-gradient(90deg,#c8232b 0%,#8a1c20 30%,#8a6a3a 60%,#b88a52 100%)" role="img" aria-label="Red log hauler truck model"></div><div class="scale">1/64 Scale</div><h3>School Bus KT Bus Internal<br>Combustion (ICE) School Bus</h3><div class="price">$545.99</div><span class="btn-outline">Add to cart</span></div>
      <div class="prod deep"><div class="prod-img soft" style="background:linear-gradient(90deg,#1d3a7a 0%,#5a6070 30%,#f4f6f8 55%,#e6e8ec 100%)" role="img" aria-label="Semi truck with white trailer model"></div><div class="scale">1/64 Scale</div><h3>School Bus KT Bus Internal<br>Combustion (ICE) School Bus</h3><div class="price">$545.99</div><span class="btn-outline">Add to cart</span></div>
      <div class="prod dark"><div class="prod-img soft" style="background:linear-gradient(90deg,#c8232b 0%,#a01d22 30%,#eef0f3 55%,#d9dce1 100%)" role="img" aria-label="Red cab semi truck with white trailer model"></div><div class="scale">1/64 Scale</div><h3>School Bus KT Bus Internal<br>Combustion (ICE) School Bus</h3><div class="price">$545.99</div><span class="btn-outline">Add to cart</span></div>
      <div class="prod blue"><div class="prod-img soft" style="background:linear-gradient(90deg,#e9ecef 0%,#c8232b 40%,#b01e24 65%,#dfe2e6 100%)" role="img" aria-label="Red truck cab model"></div><div class="scale">1/64 Scale</div><h3>School Bus KT Bus Internal<br>Combustion (ICE) School Bus</h3><div class="price">$545.99</div><span class="btn-outline">Add to cart</span></div>
    </div>
    <div class="center"><span class="btn-solid">VIEW ALL PRODUCTS</span></div>
  </div>
</section>

<section class="confidence">
  <div class="wrap">
    <div class="sec-head">
      <h2 class="h-sec"><span class="o">COLLECT WITH</span> CONFIDENCE</h2>
      <p style="width:520px">Build your dream collection with premium die-cast cars from trusted brands. Enjoy authentic models, detailed craftsmanship, secure shopping.</p>
    </div>
    <div class="conf-grid">
      <div class="conf blue">
        <svg width="44" height="40" viewBox="0 0 44 40" fill="#fff"><rect x="2" y="14" width="30" height="22" rx="3"/><path d="M32 2l10 4v8c0 7-4 11-10 13-6-2-10-6-10-13V6z" stroke="#0677ba" stroke-width="2"/><path d="M27 14l4 4 6-7" stroke="#0677ba" stroke-width="2.5" fill="none"/></svg>
        <h4>Safe &amp; Secure</h4><p>Pay Safely Using CoinDrift<br>Or Zellpay.</p>
      </div>
      <div class="conf orange">
        <svg width="46" height="40" viewBox="0 0 46 40" fill="#fff"><rect x="8" y="8" width="22" height="20" rx="2"/><path d="M30 14h8l6 7v7H30z"/><circle cx="15" cy="31" r="4"/><circle cx="36" cy="31" r="4"/><rect x="0" y="12" width="6" height="2"/><rect x="2" y="18" width="6" height="2"/></svg>
        <h4>Free Delivery</h4><p>Reliable Shipping Across<br>The United States.</p>
      </div>
      <div class="conf dark">
        <svg width="44" height="44" viewBox="0 0 44 44"><circle cx="22" cy="22" r="20" fill="#fff"/></svg>
        <h4>Guaranteed Certified</h4><p>Premium Hobby Brands<br>Collectibles.</p>
      </div>
      <div class="conf deep">
        <svg width="40" height="40" viewBox="0 0 40 40" fill="#fff"><rect x="4" y="14" width="32" height="8" rx="1"/><rect x="7" y="24" width="26" height="14" rx="1"/><rect x="18" y="14" width="4" height="24" fill="#ee7325"/><path d="M20 14c-6-10-14-4-8 0zM20 14c6-10 14-4 8 0z"/></svg>
        <h4>Free Gift Wrapping</h4><p>Select at checkout<br>Built by hobby enthusiasts</p>
      </div>
    </div>
  </div>
</section>

<section class="brands">
  <div class="wrap">
    <div class="sec-head">
      <h2 class="h-sec"><span class="o">SHOP BY</span> BRAND</h2>
      <p style="width:400px">Find your favorite die-cast brands, from legendary classics to modern performance icons.</p>
    </div>
    <div class="brand-row">
      <span class="brand-name"><span class="sq"></span>Castline Models</span>
      <span class="brand-name">Motorvale</span>
      <span class="brand-name">Verdant Lane</span>
      <span class="brand-name"><span class="sq"></span>Beacon Rail</span>
      <span class="brand-name">Gearfront</span>
    </div>
  </div>
</section>

<section class="reviews">
  <div class="wrap">
    <div class="sec-head">
      <h2 class="h-sec"><span class="o">OUR CLIENT</span> REVIEWS</h2>
      <p style="width:520px">See why collectors across the country trust us for authentic die-cast models, exceptional service, and a seamless shopping experience.</p>
    </div>
  </div>
  <div class="rev-grid">
    <div class="rev dark"><div class="stars">★★★★★</div><p>"The packaging was excellent and the model arrived in perfect condition. The detailing on the car is incredible, and it looks even better in person. Will definitely be ordering again."</p><div class="reviewer"><span class="avatar"></span><div>Dana R.<small>— Mira, Marketing Manager</small></div></div></div>
    <div class="rev orange"><div class="stars">★★★★★</div><p>"As a collector, authenticity matters a lot. The selection here is fantastic, and I found models that were sold out everywhere else. Fast shipping and great customer service too!"</p><div class="reviewer"><span class="avatar"></span><div>Lena T.<small>— Mira, Marketing Manager</small></div></div></div>
    <div class="rev blue"><div class="stars">★★★★★</div><p>"I've purchased multiple die-cast models from this store and every experience has been smooth. The quality, variety, and attention to collectors' needs make this my go-to shop."</p><div class="reviewer"><span class="avatar"></span><div>Omar S.<small>— Mira, Marketing Manager</small></div></div></div>
  </div>
  <span class="arrow" style="left:18px">‹</span>
  <span class="arrow" style="right:18px">›</span>
</section>

<section class="faq">
  <div class="sec-head">
    <h2 class="h-sec"><span class="o">FREQUENTLY ASKED</span> QUESTIONS</h2>
    <p>The models collectors can't stop talking about. bring back hands-on entertainment, collecting, building, and imagination.</p>
  </div>
  <div class="faq-list">
    <div class="faq-item"><span>What types of hobbies do you specialize in?</span><div class="faq-plus blue">+</div></div>
    <div class="faq-item"><span>Do you offer pre-orders?</span><div class="faq-plus orange">+</div></div>
    <div class="faq-item"><span>How are products shipped?</span><div class="faq-plus blue">+</div></div>
    <div class="faq-open">Can I pay with CoinDrift or Zellpay?
      <p>Yes! Copper Kite Pastimes accepts both CoinDrift and Zellpay for secure and convenient checkout. Simply select your preferred payment method during the checkout process to complete your purchase safely and quickly. If you experience any payment issues, feel free to contact us for assistance.</p>
    </div>
  </div>
</section>

<section class="cta">
  <div class="cta-card">
    <h2>Ready to start your<br>next hobby adventure?</h2>
    <p>explore collectibles, trains, slot cars, and hobby products designed to bring creativity and excitement back into everyday life.</p>
    <span class="btn-outline">SHOP PRODUCTS</span>
  </div>
  <div class="cta-art">
    <div class="cta-frame"></div>
    <div class="cta-photo" role="img" aria-label="Close-up of a blue vintage race car model"></div>
  </div>
</section>

<footer class="footer">
  <div class="foot-grid">
    <div class="foot-brand">
      <div class="foot-logo"><span class="brand-mark"></span>Copper Kite<br>Pastimes</div>
      <p>Harbor Thistle is dedicated to raising awareness, sharing experiences, and supporting individuals living with Lyme disease and chronic illness.</p>
    </div>
    <div class="foot-col"><h5>Quick Links</h5><a>Home</a><a>About</a><a>Shop by scale</a><a>Track Order</a><a>Car Models</a><a>All Products</a></div>
    <div class="foot-col" style="width:155px"><h5>Shop</h5><a>New Arrivals</a><a>Best Sellers</a><a>Brands</a><a>Vehicles</a><a>Trains</a><a>Slot Cars</a></div>
    <div class="foot-col"><h5>Connect</h5><a><span class="ic"></span>Snapgrid</a><a><span class="ic" style="border-radius:50%"></span>Friendwall</a><a><span class="ic"></span>Vidstream</a><a><span class="ic"></span>Email</a></div>
    <div class="foot-join">
      <h5>Join The Community</h5>
      <p>Subscribe to receive updates, resources, and support delivered to your inbox.</p>
      <div class="news"><div class="news-input">Enter Your Email</div><div class="news-btn"><svg width="18" height="18" viewBox="0 0 24 24" fill="#fff"><path d="M2 11l20-9-8 20-3-8z"/></svg></div></div>
      <div class="pay"><h5>Payment</h5><div class="pay-badges"><span class="pay-badge">CoinDrift</span><span class="pay-badge">Zellpay</span></div></div>
    </div>
  </div>
  <div class="foot-bottom">
    <span>© 2026 CopperKitePastimes. All Rights Reserved.</span>
    <span class="links"><span>Privacy Policy</span><span>Terms &amp; Conditions</span><span>Accessibility Statement</span></span>
  </div>
</footer>

</body>
</html>
```